**** Business card design for VoltaNode ****

For my ICT company VoltaNode I need I need a business card design.

We design, build and host web-applications and we have our own CMS product.

Some good examples are attached.

The information should be:
Joris Tielenburg
Managing director
E: j.tielenburg@voltanode-example.nl
M: +31(0)6 57218064
T: +31(0)40 7249305
W: www.voltanode-example.nl

Address:
Berend Vlootweg 27
5612 KT Eindhoven

Industry/Entity Type

Business

Requirements
Must have
• - Use logo (see attachments)
- Double sided
- Distinctive
Nice to have
• - Place for a statement on the back-side: "Designed with knowledge, built with passion"
- HTML code (or Wordpress)
- Dark (black or dark-gray) side
- Small simple images for telephone, e-mail en Url.
- QR code (only if not disturbing), not required, just an option

```html
<!DOCTYPE html>
<html lang="en">
<head>
<meta charset="utf-8">
<title>VoltaNode business cards</title>
<link rel="stylesheet" href="https://fonts.googleapis.com/css2?family=Teko:wght@500&family=Open+Sans:wght@400;600&display=swap">
<style>
  :root {
    --backdrop: #e8e9ea;
    --paper: #ffffff;
    --ink: #111111;
    --ink-light: #e4e6e8;
    --night: #0c0c0d;
    --accent: #2b97d3;
    --brand: #4a7fa6;
    --rule-light: #9a9a9a;
    --rule-dark: #8a8a8a;
    --edge: #c9c9c9;
  }
  * { margin: 0; padding: 0; box-sizing: border-box; }
  html, body { width: 1200px; height: 927px; overflow: hidden; }
  body {
    background: var(--backdrop);
    position: relative;
    font-family: "Open Sans", Arial, sans-serif;
  }
  .card {
    position: absolute;
    width: 387px;
    height: 215px;
    overflow: hidden;
  }
  .card--light { background: var(--paper); border: 1px solid var(--edge); color: var(--ink); }
  .card--dark { background: var(--night); color: var(--ink-light); }
  .card--front.card--light { left: 200px; top: 241px; border-radius: 0 0 58px 0; }
  .card--front.card--dark  { left: 613px; top: 239px; border-radius: 0 0 58px 0; }
  .card--back.card--light  { left: 200px; top: 472px; border-radius: 0 0 0 58px; }
  .card--back.card--dark   { left: 613px; top: 471px; border-radius: 0 0 0 58px; }

  .holder { position: absolute; left: 26px; top: 32px; width: 188px; }
  .holder__name {
    font-family: "Teko", "Arial Narrow", sans-serif;
    font-weight: 500;
    font-size: 27px;
    line-height: 24px;
    letter-spacing: 0.3px;
    text-transform: uppercase;
    padding-bottom: 1px;
    border-bottom: 1px solid var(--rule-light);
  }
  .card--dark .holder__name { border-bottom-color: var(--rule-dark); }
  .holder__role { font-size: 11.5px; color: var(--accent); margin-top: 2px; }

  .brand { position: absolute; display: flex; align-items: center; gap: 6px; }
  .brand__mark { border-radius: 50%; background: var(--brand); flex: none; }
  .brand__name { color: var(--brand); font-weight: 400; }
  .brand--small { right: 18px; top: 36px; }
  .brand--small .brand__mark { width: 30px; height: 30px; }
  .brand--small .brand__name { font-size: 15px; }
  .brand--large { left: 0; right: 0; top: 76px; justify-content: center; gap: 14px; }
  .brand--large .brand__mark { width: 74px; height: 74px; }
  .brand--large .brand__name { font-size: 36px; }

  .contact { position: absolute; left: 200px; top: 131px; font-size: 10.5px; line-height: 13px; }
  .contact__line { display: flex; gap: 4px; }
  .contact__label { color: var(--accent); width: 14px; text-align: right; }
  .contact__address { display: flex; align-items: flex-end; gap: 6px; margin-top: 5px; margin-left: -16px; }
  .contact__icon { width: 24px; height: 22px; flex: none; }

  .site { position: absolute; font-size: 11px; font-weight: 600; }
  .card--front .site { left: 26px; bottom: 5px; }
  .card--back .site { right: 20px; bottom: 6px; }
</style>
</head>
<body>

<section class="card card--front card--light">
  <div class="holder">
    <h1 class="holder__name">Joris Tielenburg</h1>
    <p class="holder__role">Managing director</p>
  </div>
  <div class="brand brand--small"><span class="brand__mark"></span><span class="brand__name">VoltaNode</span></div>
  <div class="contact">
    <p class="contact__line"><span class="contact__label">M:</span>+31(0)6 57218064</p>
    <p class="contact__line"><span class="contact__label">T:</span>+31(0)40 7249305</p>
    <div class="contact__address">
      <svg class="contact__icon" viewBox="0 0 24 22" aria-hidden="true"><path d="M2 11 L12 2 L22 11 M5 9 V21 H10 V14 H14 V21 H19 V9" fill="none" stroke="#2b97d3" stroke-width="1.6"/></svg>
      <p>Berend Vlootweg 27<br>5612 KT Eindhoven</p>
    </div>
  </div>
  <p class="site">www.voltanode-example.nl</p>
</section>

<section class="card card--front card--dark">
  <div class="holder">
    <h1 class="holder__name">Joris Tielenburg</h1>
    <p class="holder__role">Managing director</p>
  </div>
  <div class="brand brand--small"><span class="brand__mark"></span><span class="brand__name">VoltaNode</span></div>
  <div class="contact">
    <p class="contact__line"><span class="contact__label">M:</span>+31(0)6 57218064</p>
    <p class="contact__line"><span class="contact__label">T:</span>+31(0)40 7249305</p>
    <div class="contact__address">
      <svg class="contact__icon" viewBox="0 0 24 22" aria-hidden="true"><path d="M2 11 L12 2 L22 11 M5 9 V21 H10 V14 H14 V21 H19 V9" fill="none" stroke="#2b97d3" stroke-width="1.6"/></svg>
      <p>Berend Vlootweg 27<br>5612 KT Eindhoven</p>
    </div>
  </div>
  <p class="site">www.voltanode-example.nl</p>
</section>

<section class="card card--back card--light">
  <div class="brand brand--large"><span class="brand__mark"></span><span class="brand__name">VoltaNode</span></div>
  <p class="site">www.voltanode-example.nl</p>
</section>

<section class="card card--back card--dark">
  <div class="brand brand--large"><span class="brand__mark"></span><span class="brand__name">VoltaNode</span></div>
  <p class="site">www.voltanode-example.nl</p>
</section>

</body>
</html>
```